Updated flyer

we are a defence industry trainer and we are updating a course that has been running for a few years, so want a new look flyer. Please note that the flyer is A4 and we would like people to fill in the document online. Please add a tickbox for SME's free and add a call out box saying the course is NEW & UPDATED.

Industry/Entity Type

Defence

Font styles to use
Sans Serif
Other font styles liked:
• AVENIR

Colors
3176b5
01a88e
9bcb3b
fbed22
f37022

```html
<!DOCTYPE html>
<html lang="en">
<head>
<meta charset="utf-8">
<title>Trade Compliance Institute – Course Flyer</title>
<link href="https://fonts.googleapis.com/css2?family=Ubuntu:wght@400;500;700&family=Arimo:wght@400;700&display=swap" rel="stylesheet">
<style>
  :root{
    --green:#1f8f3e;
    --green-dark:#17722f;
    --blue:#3176b5;
    --red:#d9252c;
    --ink:#1e1e1e;
    --muted:#555;
    --grey-box:#cfcfcf;
    --field:#dcdcdc;
    --paper:#f4f4f4;
    --stage:#e6e3df;
  }
  *{box-sizing:border-box;margin:0;padding:0}
  html,body{width:1200px;height:1000px;overflow:hidden}
  body{background:var(--stage);font-family:"Arimo",Arial,sans-serif;color:var(--ink);position:relative}

  .sheet{position:absolute;top:100px;width:565px;height:800px;background:linear-gradient(160deg,#fafafa,var(--paper));box-shadow:0 4px 14px rgba(0,0,0,.18);overflow:hidden}
  .sheet--front{left:25px}
  .sheet--back{left:610px}

  /* brand */
  .brand{position:absolute;display:flex;align-items:center}
  .brand__mark{border-radius:50%;background:#bcd9ee;flex:none}
  .brand__name{font-family:"Ubuntu",sans-serif;font-weight:500;color:var(--green);line-height:.95;text-transform:uppercase;white-space:nowrap}

  .sheet--front .brand{left:178px;top:42px}
  .sheet--front .brand__mark{width:135px;height:135px;margin-right:20px}
  .sheet--front .brand__name{font-size:32px}

  /* new badge */
  .badge{position:absolute;left:18px;top:18px;width:140px;height:180px}
  .badge__ribbon{position:absolute;left:22px;top:0;width:44px;height:120px;background:var(--red);transform:skewY(-18deg)}
  .badge__tag{position:absolute;left:0;top:95px;width:135px;padding:6px 0;background:var(--blue);color:#fff;text-align:center;font-family:"Ubuntu",sans-serif;font-weight:700;font-size:17px;line-height:1.05;transform:rotate(-10deg);border:2px solid #fff;border-radius:4px}

  .title-band{position:absolute;left:0;top:215px;width:100%;height:82px;background:var(--green);color:#fff;font-family:"Ubuntu",sans-serif;font-weight:500;font-size:24px;line-height:1.2;text-align:center;padding-top:13px}

  .intro{position:absolute;left:22px;top:320px;width:265px;font-size:11px;line-height:1.3;color:#333;text-align:justify}
  .intro p+p{margin-top:10px}

  .dates{position:absolute;left:300px;top:322px;width:265px;height:160px;background:var(--grey-box);border-radius:12px 0 0 12px;padding:14px 0 0 25px;font-size:19px;line-height:27px}
  .dates li{list-style:none;display:flex}
  .dates .city{width:110px}

  .quote{position:absolute;background:#fff;padding:7px 12px;font-style:italic;font-size:11.5px;text-align:center;line-height:1.25;box-shadow:0 1px 3px rgba(0,0,0,.2)}

  .price{position:absolute;left:38px;top:635px;font-family:"Ubuntu",sans-serif;font-weight:500;font-size:39px;line-height:1.1}
  .price small{position:absolute;right:-2px;top:44px;font-size:9px;font-weight:400}
  .sme-band{position:absolute;left:0;top:697px;width:100%;height:34px;background:var(--green);color:#fff;font-family:"Ubuntu",sans-serif;font-weight:700;font-size:16px;text-align:center;line-height:34px}
  .subsidy{position:absolute;left:0;top:740px;width:100%;text-align:center;font-size:10px;color:var(--muted)}
  .sheet--front .contact{position:absolute;left:0;top:772px;width:100%;text-align:center;font-size:12px}

  /* back */
  .sheet--back .brand{left:22px;top:30px}
  .sheet--back .brand__mark{width:75px;height:75px;margin-right:12px}
  .sheet--back .brand__name{font-size:19px}
  .back-title{position:absolute;left:240px;top:52px;width:300px;height:62px;background:var(--green);border-radius:6px;color:#fff;font-family:"Ubuntu",sans-serif;font-weight:700;font-size:13.5px;text-align:center;padding-top:13px;line-height:1.3}
  .section-bar{position:absolute;top:135px;height:22px;background:#d3d3d3;font-weight:700;font-size:12px;line-height:22px}
  .section-bar--course{left:0;width:250px;padding-left:20px}
  .section-bar--register{left:250px;width:315px;text-align:center}

  .course-list{position:absolute;left:12px;top:162px;width:240px;list-style:none;font-size:9.4px;line-height:11.5px;color:#333}
  .course-list li::before{content:"- "}

  .form{position:absolute;left:258px;top:165px;width:295px;font-size:10px}
  .field{display:flex;align-items:center;height:20px}
  .field span{min-width:58px;padding-right:6px;white-space:nowrap}
  .field i{flex:1;height:16px;background:var(--field)}
  .checks{margin:5px 0 4px;line-height:17px}
  .box{display:inline-block;width:8px;height:8px;border:1px solid #333;margin:0 4px 0 6px;vertical-align:middle}
  .indent{padding-left:30px}
  .indent .field span{min-width:62px}
  .note{font-size:8px;font-style:italic;text-align:right;margin:14px 0 6px}
  .locations{list-style:none;padding-left:6px;line-height:12.5px}
  .locations li{display:flex}
  .locations .loc{width:82px}
  .reg-info{margin-top:10px;line-height:12px}
  .office{margin-top:6px;font-size:7.5px;line-height:11px;color:#444}
  .office div{display:flex;justify-content:space-between}

  .cancel{position:absolute;left:0;top:640px;width:240px;height:64px;background:var(--grey-box);border-radius:0 10px 10px 0;padding:6px 10px 0 10px;font-size:7.5px;line-height:9px}
  .cancel h3{font-size:11px;margin-bottom:3px}
  .register-band{position:absolute;left:0;top:715px;width:100%;height:32px;background:var(--green);color:#fff;font-family:"Ubuntu",sans-serif;font-size:19px;line-height:32px;padding-left:8px}
  .back-contact{position:absolute;left:0;top:768px;width:100%;display:flex;justify-content:space-around;font-size:10.5px}
</style>
</head>
<body>

<section class="sheet sheet--front">
  <div class="badge">
    <div class="badge__ribbon"></div>
    <div class="badge__tag">NEW<br>UPDATED</div>
  </div>
  <div class="brand">
    <div class="brand__mark"></div>
    <div class="brand__name">Trade<br>Compliance<br>Institute</div>
  </div>

  <div class="title-band">Defence, ITAR &amp; EAR Training Controls<br>from a non-U.S. Perspective Training</div>

  <div class="intro">
    <p>U.S. Export Controls are some of the most complex and stringent in the world. The U.S. Government regulates the transfer of U.S. origin goods and technical data throughout the world, with the intent of preventing unauthorised transfer of technology and know-how. These controls extend world-wide and can impact anyone dealing in U.S. controlled goods or technology.</p>
    <p>This two-day comprehensive course will give applicants a greater understanding of U.S. Export Controls from a non-U.S. perspective in practical and relevant terms.</p>
  </div>

  <ul class="dates">
    <li><span class="city">Brisbane</span>16 &amp; 17 March</li>
    <li><span class="city">Sydney</span>18 &amp; 19 March</li>
    <li><span class="city">Canberra</span>20 &amp; 23 March</li>
    <li><span class="city">Melbourne</span>24 &amp; 25 March</li>
    <li><span class="city">Adelaide</span>26 &amp; 27 March</li>
  </ul>

  <div class="quote" style="left:32px;top:518px;transform:rotate(-3deg)">"Excellent presenter<br>and coordination."</div>
  <div class="quote" style="left:205px;top:506px;transform:rotate(-5deg)">"Very informative, well<br>presented course."</div>
  <div class="quote" style="left:350px;top:534px;transform:rotate(-4deg)">"Excellent...best U.S export controls<br>training I have attended."</div>
  <div class="quote" style="left:110px;top:578px;transform:rotate(-4deg)">"Excellent structure and<br>style of presentation."</div>
  <div class="quote" style="left:325px;top:588px;transform:rotate(-4deg)">"Practical workshops<br>were fantastic."</div>

  <div class="price">$1295.00 AUD per person<small>inc GST</small></div>
  <div class="sme-band">small to Medium Enterprises FREE OF CHARGE</div>
  <div class="subsidy">Subsidised by the Defence Enterprise Growth Office (DEGO)</div>
  <div class="contact">For more information, please contact TCI on +61 (0)7 5550 1234 or hello@tci-training.example</div>
</section>

<section class="sheet sheet--back">
  <div class="brand">
    <div class="brand__mark"></div>
    <div class="brand__name">Trade<br>Compliance<br>Institute</div>
  </div>
  <div class="back-title">Defence, ITAR &amp; EAR Training Controls<br>from a non-U.S. Perspective Training</div>

  <div class="section-bar section-bar--course">2 Day Course Content</div>
  <div class="section-bar section-bar--register">Register Online or below</div>

  <ul class="course-list">
    <li>Export Control terms and conditions</li>
    <li>Export Control Reform and the impact to Australian industry</li>
    <li>Managing reclassifications</li>
    <li>Applying deminimis</li>
    <li>Understanding 600 Series &amp; limitations</li>
    <li>Understanding the Commerce Country List, Country Chart &amp; Country Groups</li>
    <li>Understanding deemed exports</li>
    <li>EAR General Prohibitions</li>
    <li>U.S. export controls jurisdictions</li>
    <li>Relevant legislation</li>
    <li>Understand U.S. authorisations</li>
    <li>Sub-licensing options &amp; requirements</li>
    <li>Applying U.S. exemptions</li>
    <li>Understanding re-exports &amp; how to obtain authorisation</li>
    <li>Australian export controls</li>
    <li>Australian / U.S. Trade Co-operation Treaty</li>
    <li>Dual &amp; third country national issues &amp; exemptions</li>
    <li>Developing a compliance framework</li>
    <li>Cloud Computing &amp; other technical issues</li>
    <li>Managing multi-jurisdictions</li>
    <li>Identifying the best authorisations to use</li>
    <li>Recordkeeping &amp; administrative requirements</li>
    <li>Understanding FMS</li>
    <li>Creating a monitoring &amp; self-assessment process</li>
    <li>Managing violations</li>
    <li>Non-compliance &amp; fines</li>
    <li>Case Studies</li>
    <li>Best practice principles</li>
    <li>Strategic planning</li>
  </ul>

  <form class="form">
    <div class="field"><span>Name:</span><i></i></div>
    <div class="field"><span>Company:</span><i></i></div>
    <div class="field"><span>Address:</span><i></i></div>
    <div class="field"><span>Mobile no:</span><i></i></div>
    <div class="field"><span>Email:</span><i></i></div>
    <div class="field"><span>Dietary needs:</span><i></i></div>
    <div class="checks">
      Payment method:(please check one)<br>
      <span class="box"></span>Invoice &nbsp;&nbsp;&nbsp;&nbsp;&nbsp;&nbsp;<span class="box"></span>Free of Charge (SME)<br>
      <span class="box"></span>Credit card*
    </div>
    <div class="indent">
      <div>Card type: <span class="box"></span>Globecard <span class="box"></span>Pointpay <span class="box"></span>Amerix</div>
      <div class="field"><span>Card name:</span><i></i></div>
      <div class="field"><span>Card number:</span><i></i></div>
      <div class="field"><span>Expiry date:</span><i></i></div>
      <div class="field"><span>Cardholder email:</span><i></i></div>
    </div>
    <p class="note">Credit card payments incur a 2.5% surcharge. Amerix incurs 3%.</p>
    <div>Course location:(please check)</div>
    <ul class="locations">
      <li><span class="box"></span><span class="loc">Brisbane</span>16 &amp; 17 March</li>
      <li><span class="box"></span><span class="loc">Sydney</span>18 &amp; 19 March</li>
      <li><span class="box"></span><span class="loc">Canberra</span>20 &amp; 23 March</li>
      <li><span class="box"></span><span class="loc">Melbourne</span>24 &amp; 25 March</li>
      <li><span class="box"></span><span class="loc">Adelaide</span>26 &amp; 27 March</li>
    </ul>
    <div class="reg-info">Register online @ tci-training.example/events<br>or/.. email registrations to hello@tci-training.example<br>or/.. fax to +61 (0)7 5550 5678</div>
    <div class="office">
      OFFICE USE ONLY:
      <div><span>Confirmation sent: ..........................</span><span>Invoice no: ..........................</span></div>
      <div><span>Contact person: ..........................</span><span>Paid: ..........................</span></div>
    </div>
  </form>

  <div class="cancel">
    <h3>Cancellation Policy</h3>
    Cancellations incur a 20% administration fee. No cancellations permitted within 30 days of training commencing. If a registered attendee is unable to attend, a replacement attendee is allowed.
  </div>

  <div class="register-band">REGISTER ONLINE @ tci-training.example/events</div>
  <div class="back-contact">
    <span><b>CONTACT:</b></span>
    <span>t. +61 (0)7 5550 1234</span>
    <span>e. hello@tci-training.example</span>
    <span>www.tci-training.example</span>
  </div>
</section>

</body>
</html>
```